Logo for a recruitment consultancy and executive search firm
The Ashcombe Reeve Partnership
Logo for a recruitment consultancy and executive search firm - Consulting
Creative Brief
Professional
Marian Colbeck
Head of Practice
London office: Belgrove Court 42 Belgrove Court Mayfair London W1K 4PL Dublin office: Block C The Larchfield House Oakpark, Kilbarrow Dublin, 9
marian@ashcombe-reeve.example
www.ashcombe-reeve.example
We will need 3 other business cards details are as follows: Name: Tarek Haddadi Title: Head of Practice Address: London office: Belgrove Court 42 Belgrove Court Mayfair London W1K 4PL Dublin office: Block C The Larchfield House Oakpark, Kilbarrow Dublin, 9 Phone: 020 7946 0321 Mobile: 07700900482 Email: tarek@ashcombe-reeve.example Name: Judith Purcell Title: CEO Address: London office: Belgrove Court 42 Belgrove Court Mayfair London W1K 4PL Dublin office: Block C The Larchfield House Oakpark, Kilbarrow Dublin, 9 Phone: 020 7946 0321 Mobile: 07700 900 615 Email: judith@ashcombe-reeve.example Name: Helen Varty Title: Finance Manager Address: London office: Belgrove Court 42 Belgrove Court Mayfair London W1K 4PL Dublin office: Block C The Larchfield House Oakpark, Kilbarrow Dublin, 9 0321 Mobile: 07700 900 738 email: accounts@ashcombe-reeve.example We want the complete stationary set! The more the merrier as far as I am concerned. folders compliment strips headed paper email signature envelopes presentation format position documents folder you name it we want it!
Black with Ashcombe reeve logo

```html
<!DOCTYPE html>
<html lang="en">
<head>
<meta charset="utf-8">
<title>The Ashcombe Reeve Partnership – Business Cards</title>
<link href="https://fonts.googleapis.com/css2?family=Cinzel:wght@400;600&display=swap" rel="stylesheet">
<style>
  :root {
    --backdrop: #d9d9d9;
    --card-black: #1e1a18;
    --card-white: #ffffff;
    --ink-light: #f2f2f2;
    --ink-muted: #bdbdbd;
  }
  html, body {
    margin: 0;
    padding: 0;
    width: 1200px;
    height: 987px;
    overflow: hidden;
    background: var(--backdrop);
    font-family: "Cinzel", serif;
  }
  .canvas {
    position: relative;
    width: 1200px;
    height: 987px;
  }
  .card {
    position: absolute;
    background: var(--card-black);
    border-radius: 22px;
    overflow: hidden;
    box-shadow: 0 18px 30px rgba(0,0,0,0.25);
    color: var(--ink-light);
  }
  /* Back of card */
  .card-back {
    left: 130px;
    top: 80px;
    width: 620px;
    height: 354px;
  }
  .card-back .brand {
    position: absolute;
    left: 0; right: 0;
    top: 120px;
    display: flex;
    align-items: center;
    justify-content: center;
    gap: 14px;
  }
  .brand-dot {
    width: 22px;
    height: 22px;
    border-radius: 50%;
    background: var(--ink-light);
  }
  .brand-name {
    font-size: 30px;
    font-weight: 400;
    letter-spacing: 3px;
    text-transform: uppercase;
    color: var(--ink-light);
  }
  .card-back .web {
    position: absolute;
    left: 0; right: 0;
    top: 210px;
    text-align: center;
    font-size: 11px;
    letter-spacing: 5px;
    text-transform: uppercase;
    color: var(--ink-muted);
  }
  /* Front of card */
  .card-front {
    left: 360px;
    top: 500px;
    width: 720px;
    height: 410px;
  }
  .card-front .swoosh {
    position: absolute;
    inset: 0;
    width: 100%;
    height: 100%;
  }
  .front-brand {
    position: absolute;
    left: 40px;
    top: 118px;
    width: 330px;
    text-align: center;
  }
  .front-brand .brand-dot {
    margin: 0 auto 12px;
  }
  .front-brand .brand-name {
    font-size: 27px;
    letter-spacing: 2px;
    display: block;
  }
  .front-brand .brand-sub {
    display: block;
    font-size: 15px;
    letter-spacing: 4px;
    text-transform: uppercase;
    border-top: 1px solid var(--ink-muted);
    margin: 6px 40px 0;
    padding-top: 4px;
  }
  .person {
    position: absolute;
    left: 40px;
    top: 262px;
  }
  .person-name {
    font-size: 18px;
    letter-spacing: 1px;
    margin: 0;
    font-weight: 400;
  }
  .person-title {
    font-size: 11px;
    letter-spacing: 2px;
    text-transform: uppercase;
    color: var(--ink-muted);
    margin: 6px 0 0;
  }
  .contact-list {
    position: absolute;
    left: 400px;
    top: 262px;
    margin: 0;
    padding: 0;
    list-style: none;
    font-size: 10px;
    letter-spacing: 0.5px;
    line-height: 19px;
  }
  .contact-list li {
    display: flex;
    align-items: flex-start;
    gap: 8px;
  }
  .contact-icon {
    flex: 0 0 auto;
    width: 13px;
    height: 13px;
    margin-top: 3px;
  }
</style>
</head>
<body>
<div class="canvas">

  <section class="card card-back">
    <div class="brand">
      <span class="brand-dot"></span>
      <span class="brand-name">Ashcombe Reeve</span>
    </div>
    <div class="web">www.ashcombe-reeve.example</div>
  </section>

  <section class="card card-front">
    <svg class="swoosh" viewBox="0 0 720 410" aria-hidden="true">
      <path d="M150 0 L720 0 L720 410 L665 410 C620 210 430 55 150 0 Z" fill="var(--card-white)"/>
      <path d="M200 6 C440 40 610 150 690 350" fill="none" stroke="var(--card-black)" stroke-width="9" stroke-linecap="round"/>
      <path d="M230 2 C450 30 630 130 712 300" fill="none" stroke="var(--card-black)" stroke-width="3"/>
    </svg>

    <div class="front-brand">
      <span class="brand-dot"></span>
      <span class="brand-name">Ashcombe Reeve</span>
      <span class="brand-sub">Partnership</span>
    </div>

    <div class="person">
      <h2 class="person-name">Marian Colbeck</h2>
      <p class="person-title">Head of Practice</p>
    </div>

    <ul class="contact-list">
      <li>
        <svg class="contact-icon" viewBox="0 0 14 14" aria-hidden="true"><circle cx="7" cy="7" r="7" fill="var(--ink-light)"/><path d="M7 3a2.4 2.4 0 0 0-2.4 2.4C4.6 7.4 7 11 7 11s2.4-3.6 2.4-5.6A2.4 2.4 0 0 0 7 3z" fill="var(--card-black)"/></svg>
        <span>Block C The Larchfield House<br>Oakpark, Kilbarrow Dublin, 9</span>
      </li>
      <li>
        <svg class="contact-icon" viewBox="0 0 14 14" aria-hidden="true"><circle cx="7" cy="7" r="7" fill="var(--ink-light)"/><path d="M4.5 3.5l1.5-.3 1 2-1 .8a5 5 0 0 0 2 2l.8-1 2 1-.3 1.5c-3 .5-6.5-3-6-6z" fill="var(--card-black)"/></svg>
        <span>020 7946 0321</span>
      </li>
      <li>
        <svg class="contact-icon" viewBox="0 0 14 14" aria-hidden="true"><circle cx="7" cy="7" r="7" fill="var(--ink-light)"/><rect x="5" y="3" width="4" height="8" rx="0.8" fill="var(--card-black)"/></svg>
        <span>07700900482</span>
      </li>
      <li>
        <svg class="contact-icon" viewBox="0 0 14 14" aria-hidden="true"><circle cx="7" cy="7" r="7" fill="var(--ink-light)"/><rect x="3.5" y="4.5" width="7" height="5" fill="var(--card-black)"/><path d="M3.5 4.5L7 7.4l3.5-2.9" fill="none" stroke="var(--ink-light)" stroke-width="0.7"/></svg>
        <span>marian@ashcombe-reeve.example</span>
      </li>
      <li>
        <svg class="contact-icon" viewBox="0 0 14 14" aria-hidden="true"><circle cx="7" cy="7" r="7" fill="var(--ink-light)"/><circle cx="7" cy="7" r="3.6" fill="none" stroke="var(--card-black)" stroke-width="0.9"/><path d="M3.4 7h7.2M7 3.4c-1.6 2-1.6 5.2 0 7.2M7 3.4c1.6 2 1.6 5.2 0 7.2" fill="none" stroke="var(--card-black)" stroke-width="0.7"/></svg>
        <span>www.ashcombe-reeve.example</span>
      </li>
    </ul>
  </section>

</div>
</body>
</html>
```